Larkspur Elementary
Stationary, Letterhead, Business Card
Simple
Cora P. Wendt
Counselor
742 Ridgeway Lane
Hollowmere, XX 00123
wendt_cora@mbxsd.org
http://les.hollowmere.k12.xx.us
I would like to stay with the navy gold and blue theme (but variations are fine) but a white background is not necessary.
I like the vertical look more than the horizontal but both are welcomed.
If you follow the link, I like how #8, #15, and #18 look format-wise.
I look forward to your designs.
http://www.quarvelblog.com/2008/06/25/yet-another-post-with-unique-business-cards/
Logo plus your creative touches

```html
<!DOCTYPE html>
<html lang="en">
<head>
<meta charset="utf-8">
<title>Larkspur Elementary Counseling – Business Card</title>
<link href="https://fonts.googleapis.com/css2?family=Roboto+Condensed:wght@400;700&display=swap" rel="stylesheet">
<style>
  :root {
    --gold: #e0a526;
    --gold-deep: #b97a12;
    --gold-light: #f7cf5a;
    --navy: #1b2f7a;
    --blue: #2f6fd0;
    --sky: #39b6ec;
    --ink: #1a1a1a;
    --grey: #b8b8b8;
    --paper: #ffffff;
  }
  * { margin: 0; padding: 0; box-sizing: border-box; }
  html, body { width: 1200px; height: 871px; overflow: hidden; background: var(--paper); }
  body { position: relative; font-family: "Roboto Condensed", "Arial Narrow", sans-serif; color: var(--ink); }

  .card {
    position: absolute; top: 108px; width: 388px; height: 684px;
    background: var(--paper); overflow: hidden;
    box-shadow: 0 4px 14px rgba(0,0,0,.28);
  }
  .card--front { left: 151px; }
  .card--back { left: 549px; }

  .gold-band {
    position: absolute; left: 0; top: 0; width: 78px; height: 100%;
    background: linear-gradient(90deg, var(--gold-deep), var(--gold) 45%, var(--gold-light) 80%, var(--gold));
  }
  .sky-band {
    position: absolute; right: 0; top: 0; width: 50px; height: 100%;
    background: linear-gradient(180deg, var(--sky) 0%, #4aa9e8 55%, var(--blue) 80%, var(--navy) 100%);
  }
  .back-wave { position: absolute; left: 0; bottom: 0; width: 100%; height: 200px; }

  .brand { position: absolute; display: flex; align-items: center; gap: 8px; }
  .brand__mark { width: 16px; height: 16px; background: var(--navy); flex: none; }
  .brand__name {
    font-weight: 700; color: var(--navy); text-transform: uppercase; line-height: 1.05; white-space: nowrap;
  }
  .brand--front { left: 30px; top: 44px; }
  .brand--front .brand__name { font-size: 22px; }

  .art { position: absolute; }
  .art--gold { left: 233px; top: 204px; width: 165px; height: 408px; border-radius: 48px 0 0 48px; }
  .art--blue { left: 0; top: 204px; width: 170px; height: 408px; border-radius: 0 48px 48px 0; }

  .person { position: absolute; right: 58px; top: 354px; text-align: right; }
  .person__name { font-size: 30px; font-weight: 700; letter-spacing: .5px; text-transform: uppercase; white-space: nowrap; }
  .person__role { font-size: 20px; margin-top: 2px; }

  .contact {
    position: absolute; right: 46px; top: 548px; font-size: 14px; line-height: 24px;
    text-align: right; white-space: nowrap;
  }

  .vertical-email {
    position: absolute; font-size: 15px; font-weight: 700; white-space: nowrap;
    transform-origin: left top; color: var(--ink);
  }
  .vertical-email--front { left: 30px; top: 500px; transform: rotate(90deg) translateY(-100%); }
  .vertical-email--back { left: 365px; top: 30px; transform: rotate(90deg) translateY(-100%); }

  .brand--back { left: 66px; top: 330px; }
  .brand--back .brand__name { font-size: 18px; }

  .web { position: absolute; left: 70px; top: 636px; font-size: 16px; font-weight: 700; white-space: nowrap; }

  .brand--grey { left: 960px; top: 592px; }
  .brand--grey .brand__mark { background: var(--grey); width: 20px; height: 20px; }
  .brand--grey .brand__name { color: var(--grey); font-size: 22px; }
  .brand__tag { font-size: 10px; letter-spacing: 1px; color: var(--grey); display: block; margin-top: 3px; font-weight: 400; }
</style>
</head>
<body>

  <section class="card card--front">
    <div class="gold-band"></div>
    <div class="brand brand--front">
      <span class="brand__mark"></span>
      <span class="brand__name">Larkspur<br>Elementary Counseling</span>
    </div>
    <div class="art art--gold" role="img" aria-label="Large gold decorative shape"
         style="background: radial-gradient(circle at 40% 30%, var(--gold-light), var(--gold) 55%, var(--gold-deep));"></div>
    <div class="person">
      <div class="person__name">Cora P. Wendt</div>
      <div class="person__role">Counselor</div>
    </div>
    <div class="contact">
      742 Ridgeway Lane Hollowmere, XX 00123<br>
      Phone: 555.014.7710<br>
      Fax: 555.014.7788
    </div>
    <div class="vertical-email vertical-email--front">wendt_cora@mbxsd.org</div>
  </section>

  <section class="card card--back">
    <div class="sky-band"></div>
    <svg class="back-wave" viewBox="0 0 388 200" preserveAspectRatio="none" aria-hidden="true">
      <defs>
        <linearGradient id="waveFill" x1="0" y1="0" x2="1" y2="0">
          <stop offset="0" stop-color="#ffffff" stop-opacity="0"/>
          <stop offset="1" stop-color="#2f6fd0" stop-opacity=".35"/>
        </linearGradient>
      </defs>
      <path d="M0 200 L388 200 L388 20 Q300 140 0 190 Z" fill="url(#waveFill)"/>
    </svg>
    <div class="art art--blue" role="img" aria-label="Large blue decorative shape"
         style="background: radial-gradient(circle at 60% 30%, #6fa8ef, var(--blue) 50%, var(--navy));"></div>
    <div class="brand brand--back">
      <span class="brand__mark"></span>
      <span class="brand__name">Larkspur<br>Elementary Counseling</span>
    </div>
    <div class="vertical-email vertical-email--back">wendt_cora@mbxsd.org</div>
    <div class="web">http://les.hollowmere.k12.xx.us</div>
  </section>

  <div class="brand brand--grey">
    <span class="brand__mark"></span>
    <span class="brand__name">Larkspur<br>Elementary<br>Counseling<span class="brand__tag">HELPING EVERY STUDENT</span></span>
  </div>

</body>
</html>
```